Business Card

We need some ideas for corporate business cards. I'm interested in a double sided card, with one side featuring our corporate logo, the other side with employee information.

Corporate colors, logo etc. available at www.varnik.com

Industry/Entity Type

Business

Requirements
Must have
• The "Varnik" logo with stylized "O"

Nice to have
• Preferred font is calibri

```html
<!DOCTYPE html>
<html lang="en">
<head>
<meta charset="utf-8">
<title>Varnik Business Card</title>
<link href="https://fonts.googleapis.com/css2?family=Montserrat:wght@400;600;700&display=swap" rel="stylesheet">
<style>
  :root {
    --backdrop: #7d7d7d;
    --brand-blue: #2f5e9c;
    --paper: #f4f4f2;
    --white: #ffffff;
    --photo-tone-a: #b9a58f;
    --photo-tone-b: #3b4a5e;
  }
  * { box-sizing: border-box; margin: 0; padding: 0; }
  html, body { width: 1200px; height: 873px; overflow: hidden; }
  body {
    background: var(--backdrop);
    font-family: "Montserrat", "Calibri", sans-serif;
    position: relative;
  }
  .card {
    position: absolute;
    top: 156px;
    width: 360px;
    height: 560px;
    overflow: hidden;
    box-shadow: 0 10px 30px rgba(0,0,0,0.25);
  }
  .card--front { left: 200px; background: var(--brand-blue); }
  .card--back { left: 640px; background: var(--brand-blue); }

  /* Front */
  .tagline {
    position: absolute; left: 34px; top: 44px;
    color: var(--white); font-weight: 700; font-size: 27px;
    line-height: 1.02; letter-spacing: 1.5px; text-transform: uppercase;
  }
  .service-icons {
    position: absolute; left: 34px; top: 170px;
    display: flex; gap: 22px;
  }
  .service-icon { width: 30px; display: flex; flex-direction: column; align-items: center; gap: 8px; }
  .service-icon svg { width: 24px; height: 24px; }
  .service-icon .tick { width: 1px; height: 12px; background: var(--white); opacity: 0.8; }
  .front-footer {
    position: absolute; left: 0; right: 0; bottom: 0; height: 160px;
    background: var(--paper);
    display: flex; align-items: center; justify-content: flex-end;
    padding-right: 32px;
  }
  .wordmark {
    display: flex; align-items: center; gap: 10px;
    color: var(--brand-blue); font-weight: 600; font-size: 36px; letter-spacing: 3px;
  }
  .wordmark .dot { width: 16px; height: 16px; background: var(--brand-blue); border-radius: 50%; }

  /* Back */
  .back-header {
    position: absolute; left: 0; right: 0; top: 0; height: 190px;
    background: var(--white);
  }
  .portrait {
    position: absolute; left: 28px; top: 34px; width: 92px; height: 96px;
    background: linear-gradient(180deg, var(--photo-tone-a) 0%, var(--photo-tone-a) 55%, var(--photo-tone-b) 100%);
  }
  .employee {
    position: absolute; left: 140px; top: 42px;
    color: var(--brand-blue); font-size: 12.5px; line-height: 1.35; text-transform: uppercase;
  }
  .employee .name { font-weight: 400; }
  .employee .role { font-weight: 700; font-size: 11px; margin-bottom: 14px; }
  .label { font-weight: 700; }
  .company-info {
    position: absolute; left: 40px; top: 228px;
    color: var(--white); font-size: 12.5px; line-height: 1.35; text-transform: uppercase;
  }
  .company-info .address { margin-bottom: 14px; }
  .company-info .website { font-weight: 700; margin-top: 22px; }
</style>
</head>
<body>

<section class="card card--front" aria-label="Card front">
  <h1 class="tagline">Intelligent<br>Digital<br>Solutions</h1>
  <div class="service-icons">
    <div class="service-icon">
      <svg viewBox="0 0 24 24" aria-hidden="true">
        <g fill="#fff">
          <circle cx="12" cy="12" r="7"/>
          <rect x="10.5" y="1.5" width="3" height="5"/>
          <rect x="10.5" y="17.5" width="3" height="5"/>
          <rect x="1.5" y="10.5" width="5" height="3"/>
          <rect x="17.5" y="10.5" width="5" height="3"/>
          <rect x="10.5" y="1.5" width="3" height="5" transform="rotate(45 12 12)"/>
          <rect x="10.5" y="17.5" width="3" height="5" transform="rotate(45 12 12)"/>
          <rect x="1.5" y="10.5" width="5" height="3" transform="rotate(45 12 12)"/>
          <rect x="17.5" y="10.5" width="5" height="3" transform="rotate(45 12 12)"/>
        </g>
        <circle cx="12" cy="12" r="3" fill="#2f5e9c"/>
      </svg>
      <span class="tick"></span>
    </div>
    <div class="service-icon">
      <svg viewBox="0 0 24 24" aria-hidden="true">
        <circle cx="12" cy="12" r="10" fill="#fff"/>
        <circle cx="12" cy="12" r="7.5" fill="#2f5e9c"/>
        <path d="M16 8 L13.2 13.2 L8 16 L10.8 10.8 Z" fill="#fff"/>
      </svg>
      <span class="tick"></span>
    </div>
    <div class="service-icon">
      <svg viewBox="0 0 24 24" aria-hidden="true">
        <path d="M1 12 C5 5, 19 5, 23 12 C19 19, 5 19, 1 12 Z" fill="#fff"/>
        <circle cx="12" cy="12" r="4.5" fill="#2f5e9c"/>
        <circle cx="12" cy="12" r="2" fill="#fff"/>
      </svg>
      <span class="tick"></span>
    </div>
  </div>
  <div class="front-footer">
    <div class="wordmark"><span class="dot"></span>VARNIK</div>
  </div>
</section>

<section class="card card--back" aria-label="Card back">
  <div class="back-header">
    <div class="portrait" role="img" aria-label="Employee portrait photograph"></div>
    <div class="employee">
      <div class="name">Alan Reed</div>
      <div class="role">Executive Director</div>
      <div><span class="label">Tel:</span> (+353) 1 555 0140</div>
      <div><span class="label">Fax:</span> (+353) 1 555 0199</div>
      <div>alan.reed@varnik.com</div>
    </div>
  </div>
  <div class="company-info">
    <div class="address">
      14 Harbour Lane<br>
      Westgate Business Park<br>
      Dublin 8<br>
      Dublin, DB
    </div>
    <div><span class="label">Tel:</span> (+353) 1 555 0140</div>
    <div><span class="label">Fax:</span> (+353) 1 555 0199</div>
    <div>info@varnik.com</div>
    <div class="website">varnik.com</div>
  </div>
</section>

</body>
</html>
```